Poster design for the MIRUM VELUM magic show.

We need a poster design for our magic show. This isn't your typical 'small town' magic show. Our show features world class magicians from the Wonder Lantern, in Hollywood California. The show is geared toward everyone, it is family friendly - with a little bit of an edge. We want people to see the poster and feel like they are going to have a unique and sophisticated magical experience. We also want individuals and couples to see the poster and feel like it is a show for them and not only for children.
Updates

Target Market(s)

WBC audience, family audience, the age range is anywhere from 5 - 105. Cool people.

Industry/Entity Type

Town

Requirements
Must have
• Our attached .jpg of the magician floating in the air. Poster size 24x36"
Must have text:
The 3rd Annual Albuquerque Conjuring Revue Presents (small type)
Mirum Velum (should be larger type)
November 24th - 25th
Showtimes 3:00PM & 7:30PM Saturday, 2:00PM Sunday
Tickets available at www.ZelaraSeats.example For more information contact Zelara Theatre @ 505.241.9067
Nice to have
• A sort of old school/antique feeling to the poster.
Perhaps a theater marquee
Check out www.tundravelvet.example - we love the feeling of this site for our poster...
Feel free to adjust the provided .jpg accordingly in regards to color/size/interaction with the rest of the poster
Should not have
• Should not have clowns, bunnies, anything that would make it feel like a 3 year old's magic themed birthday party.

```html
<!DOCTYPE html>
<html lang="en">
<head>
<meta charset="utf-8">
<title>Mirum Velum Poster</title>
<link rel="stylesheet" href="https://fonts.googleapis.com/css2?family=Rye&family=Cinzel:wght@500&display=swap">
<style>
  :root {
    --page: #ffffff;
    --red: #c21a02;
    --red-deep: #6a0c02;
    --maroon: #2a0400;
    --black: #0c0100;
    --gold: #a7802a;
    --ink: #120200;
    --white: #ffffff;
  }
  html, body {
    margin: 0;
    width: 1200px;
    height: 900px;
    overflow: hidden;
    background: var(--page);
  }
  .poster {
    position: absolute;
    left: 330px;
    top: 52px;
    width: 518px;
    height: 776px;
    overflow: hidden;
    background: linear-gradient(180deg, var(--red) 0%, var(--red) 28%, var(--red-deep) 55%, var(--maroon) 66%, var(--black) 100%);
    box-shadow: 4px 4px 6px rgba(0,0,0,0.45);
  }
  .presenter {
    position: absolute;
    top: 20px;
    left: 0;
    width: 100%;
    margin: 0;
    text-align: center;
    font-family: "Rye", serif;
    font-size: 14px;
    color: var(--white);
    letter-spacing: 0.3px;
    white-space: nowrap;
  }
  .show-title {
    position: absolute;
    top: 60px;
    left: 0;
    width: 100%;
    margin: 0;
    text-align: center;
    font-family: "Rye", serif;
    font-weight: 400;
    font-size: 54px;
    line-height: 1;
    color: var(--ink);
    letter-spacing: 1px;
    text-shadow: 3px 3px 0 rgba(70,0,0,0.7);
    white-space: nowrap;
  }
  .ornate-frame {
    position: absolute;
    left: 14px;
    top: 133px;
    width: 484px;
    height: 322px;
    border-radius: 18px;
    background: radial-gradient(ellipse at center, transparent 58%, rgba(167,128,42,0.55) 74%, var(--gold) 100%);
  }
  .stage-photo {
    position: absolute;
    left: 68px;
    top: 188px;
    width: 374px;
    height: 212px;
    border: 6px solid var(--gold);
    background:
      radial-gradient(ellipse 30% 60% at 38% 10%, rgba(255,110,60,0.7), transparent 70%),
      radial-gradient(ellipse 30% 60% at 62% 10%, rgba(255,110,60,0.7), transparent 70%),
      linear-gradient(180deg, #8c2408 0%, #5a1203 60%, #2a0600 100%);
  }
  .ticket-band {
    position: absolute;
    left: 0;
    top: 466px;
    width: 100%;
    height: 42px;
    background: var(--gold);
    text-align: center;
    font-family: "Rye", serif;
    font-size: 10px;
    line-height: 17px;
    color: var(--white);
    padding-top: 4px;
    box-sizing: border-box;
    white-space: nowrap;
  }
  .ticket-band p { margin: 0; }
  .film-strip {
    position: absolute;
    left: 0;
    top: 508px;
    width: 518px;
    height: 268px;
  }
  .film-text {
    font-family: "Cinzel", serif;
    font-weight: 500;
    fill: var(--ink);
  }
</style>
</head>
<body>
  <main class="poster">
    <p class="presenter">The 3rd Annual Albuquerque Conjuring Revue Presents</p>
    <h1 class="show-title">MIRUM VELUM</h1>

    <div class="ornate-frame" role="img" aria-label="Gold filigree ornamental frame"></div>
    <div class="stage-photo" role="img" aria-label="Photo of the magician floating on a stage under red spotlights"></div>

    <div class="ticket-band">
      <p>Tickets available at www.ZelaraSeats.example</p>
      <p>For more information contact Zelara Theatre @ 505.241.9067</p>
    </div>

    <svg class="film-strip" viewBox="0 0 518 268" aria-label="Showtimes and dates on a film strip">
      <defs>
        <pattern id="sprockets" width="14" height="12" patternUnits="userSpaceOnUse">
          <rect x="2" y="2" width="9" height="8" rx="3" fill="#c21a02"/>
        </pattern>
        <radialGradient id="frameFill" cx="50%" cy="45%" r="70%">
          <stop offset="70%" stop-color="#c21a02"/>
          <stop offset="100%" stop-color="#7a0e01"/>
        </radialGradient>
      </defs>
      <rect width="518" height="268" fill="#0c0100"/>
      <g transform="rotate(-8 259 134)">
        <rect x="-80" y="40" width="700" height="24" fill="#1a0200"/>
        <rect x="-80" y="46" width="700" height="12" fill="url(#sprockets)"/>
        <rect x="-80" y="262" width="700" height="24" fill="#1a0200"/>
        <rect x="-80" y="268" width="700" height="12" fill="url(#sprockets)"/>

        <rect x="-70" y="80" width="150" height="182" fill="url(#frameFill)"/>
        <rect x="0" y="140" width="50" height="110" fill="#a7802a" opacity="0.3" role="img" aria-label="Gold swirl ornament"/>

        <rect x="98" y="74" width="240" height="188" fill="url(#frameFill)"/>
        <text class="film-text" x="130" y="122" font-size="24">Showtimes</text>
        <text class="film-text" x="126" y="160" font-size="16">3:00pm &amp; 7:30pm</text>
        <text class="film-text" x="126" y="182" font-size="20">on Saturday</text>
        <text class="film-text" x="134" y="220" font-size="17">2:00pm Sunday</text>

        <rect x="350" y="70" width="205" height="176" fill="url(#frameFill)"/>
        <text class="film-text" x="364" y="110" font-size="21">November</text>
        <text class="film-text" x="376" y="136" font-size="17">24th - 25th</text>
        <rect x="412" y="170" width="30" height="26" fill="#a7802a" opacity="0.5" role="img" aria-label="Small gold flourish ornament"/>
      </g>
    </svg>
  </main>
</body>
</html>
```